Body therapist needs a business card

I need a card for my business which is teaching trainings in body therapy, the company is called Wexcombe Educational Group. I teach to massage therapists around Australia, South East Asia and the USA. I am attaching my logo which will guide you as to what colours I would like to have you consider. Please consult my website to find out more about what I do. www.corvantela.com.au

My name is Daniel Wexcombe. My phone number is (03) 9417 2608 or 0461753208. email is info@corvantela.com.au

```html
<!DOCTYPE html>
<html lang="en">
<head>
<meta charset="utf-8">
<title>Wexcombe Educational Group – Business Card</title>
<link rel="stylesheet" href="https://fonts.googleapis.com/css2?family=Open+Sans:wght@300;400&family=Roboto:wght@500&family=Work+Sans:wght@400&display=swap">
<style>
  :root {
    --backdrop: #262626;
    --card-white: #ffffff;
    --brand-brown: #5e3322;
    --brand-red: #b20a0a;
    --ink-grey: #4a4a4a;
    --text-white: #ffffff;
  }
  * { margin: 0; padding: 0; box-sizing: border-box; }
  html, body {
    width: 1200px; height: 900px; overflow: hidden;
    background: var(--backdrop);
  }
  .card {
    position: absolute; left: 261px; width: 656px; height: 357px;
    border-radius: 24px; overflow: hidden;
  }
  .card--front { top: 69px; background: var(--card-white); }
  .card--back { top: 472px; background: var(--brand-brown); }

  .brand { position: absolute; font-family: "Open Sans", sans-serif; }
  .brand__mark {
    position: absolute; width: 80px; height: 80px; border-radius: 50%;
    background: var(--brand-brown);
  }
  .card--front .brand__mark { left: 44px; top: 135px; }
  .brand__name { font-weight: 400; line-height: 1; }
  .brand__tagline { font-weight: 300; line-height: 1; }

  .card--front .brand__name {
    position: absolute; left: 146px; top: 148px;
    font-size: 30px; color: var(--brand-brown);
  }
  .card--front .brand__tagline {
    position: absolute; left: 146px; top: 183px;
    font-size: 13px; color: var(--brand-red);
  }

  .divider {
    position: absolute; left: 353px; top: 84px; width: 2px; height: 180px;
    background: var(--brand-red);
  }

  .contact { position: absolute; left: 386px; top: 78px; }
  .contact__name {
    font-family: "Roboto", sans-serif; font-weight: 500;
    font-size: 23px; color: var(--brand-red); line-height: 1.1;
  }
  .contact__role, .contact__address, .contact__line {
    font-family: "Work Sans", sans-serif; color: var(--ink-grey);
    letter-spacing: 1px;
  }
  .contact__role { font-size: 16px; margin-top: 3px; }
  .contact__address { font-size: 14.5px; line-height: 20px; margin-top: 12px; }
  .contact__list { list-style: none; margin-top: 9px; }
  .contact__line {
    display: flex; align-items: center; font-size: 16px; height: 21.5px;
  }
  .contact__icon { width: 12px; height: 12px; margin-right: 7px; flex: none; }

  .footer-band {
    position: absolute; left: 0; top: 316px; width: 100%; height: 28px;
    display: flex;
  }
  .footer-band__brown { width: 324px; background: var(--brand-brown); }
  .footer-band__red { flex: 1; background: var(--brand-red); }

  .card--back .brand__name {
    position: absolute; left: 353px; top: 252px;
    font-size: 42px; color: var(--text-white);
  }
  .card--back .brand__tagline {
    position: absolute; left: 353px; top: 303px;
    font-size: 19px; color: var(--text-white);
  }
</style>
</head>
<body>
  <section class="card card--front">
    <div class="brand">
      <span class="brand__mark"></span>
    </div>
    <p class="brand brand__name">Wexcombe</p>
    <p class="brand brand__tagline">Educational Group</p>

    <div class="divider"></div>

    <div class="contact">
      <h1 class="contact__name">Daniel Wexcombe</h1>
      <p class="contact__role">Director</p>
      <p class="contact__address">P.O. Box 2274 Ashford Vale<br>Victoria, 3150 Australia</p>
      <ul class="contact__list">
        <li class="contact__line">
          <svg class="contact__icon" viewBox="0 0 12 12" aria-hidden="true"><path d="M3 1 L5 3.5 L4 4.8 Q5 7.2 7.2 8 L8.5 7 L11 9 L9.8 11 Q3.5 10.5 1.2 2.5 Z" fill="#b20a0a"/></svg>
          03 9417 2608
        </li>
        <li class="contact__line">
          <svg class="contact__icon" viewBox="0 0 12 12" aria-hidden="true"><rect x="3" y="0.8" width="6" height="10.4" rx="1" fill="none" stroke="#b20a0a" stroke-width="1.5"/><circle cx="6" cy="9" r="0.8" fill="#b20a0a"/></svg>
          0461753208
        </li>
        <li class="contact__line">
          <svg class="contact__icon" viewBox="0 0 12 12" aria-hidden="true"><rect x="0.8" y="2.5" width="10.4" height="7" fill="none" stroke="#b20a0a" stroke-width="1.3"/><path d="M1 3 L6 6.5 L11 3" fill="none" stroke="#b20a0a" stroke-width="1.3"/></svg>
          info@corvantela.com.au
        </li>
        <li class="contact__line">
          <svg class="contact__icon" viewBox="0 0 12 12" aria-hidden="true"><g fill="none" stroke="#b20a0a" stroke-width="1"><circle cx="6" cy="6" r="5"/><ellipse cx="6" cy="6" rx="2.2" ry="5"/><path d="M1 6 H11 M2 3.3 H10 M2 8.7 H10"/></g></svg>
          www.corvantela.com.au
        </li>
      </ul>
    </div>

    <div class="footer-band">
      <span class="footer-band__brown"></span>
      <span class="footer-band__red"></span>
    </div>
  </section>

  <section class="card card--back">
    <p class="brand brand__name">Wexcombe</p>
    <p class="brand brand__tagline">Educational Group</p>
  </section>
</body>
</html>
```